Clothing Brand E-Commerce Website Design

We would like you to provide an ecommerce design template in layered PSD for our clothing/fashion brand website called "TrelWick".
We want the site to have a simple but sleek design similar to the following sites:
http://www.pivorane.com/
http://corvatelle.com/
http://www.dulvenor.com/
We want it to look stunning and blow the example sites out of the water. For color scheme, please use your imagination and try to impress us with your creativity.
We like teal and beige pink, with teal dominant.
Teal #7AFFFF / #46C6C6
Beige/pink #FF7B7C / #C74646
We want you to develop the design for 3 pages:
1) Home Page
Samples:
http://www.pivorane.com/
http://corvatelle.com/
http://www.dulvenor.com/
2) Products List Page (e.g., lists all "Dresses" when category is selected)
http://www.pivorane.com/shop/casual-dresses
http://www.dulvenor.com/index.php?main_page=index&cPath=3
http://corvatelle.com/modest-dresses.html
http://www.quillmarsh.com/Product/Category.aspx?br=q47&category=dress_maxi
3) Product Detail Page (e.g., individual product page with "Add to Cart")
http://www.pivorane.com/shop/dresses/lumen-fern-dress
http://corvatelle.com/modest-dresses/modest-dress-tova.html
http://www.dulvenor.com/index.php?main_page=product_info&cPath=3&products_id=297
Industry/Entity Type
Fashion

```html
<!DOCTYPE html>
<html lang="en">
<head>
<meta charset="utf-8">
<title>TrelWick</title>
<link href="https://fonts.googleapis.com/css2?family=Lato:wght@400;700&display=swap" rel="stylesheet">
<style>
:root{
  --teal:#46c6c6;
  --teal-line:#6fd3d3;
  --coral:#ff7b7c;
  --bg:#ececec;
  --white:#ffffff;
  --text:#333333;
  --muted:#e6e6e6;
  --rule:#bdbdbd;
}
*{box-sizing:border-box;margin:0;padding:0}
html,body{width:1200px;height:1098px;overflow:hidden}
body{background:var(--bg);font-family:'Lato',sans-serif;color:var(--text);position:relative}
.site-header{position:absolute;left:0;top:0;width:1200px;height:137px;background:var(--teal)}
.top-bar{position:absolute;left:50px;top:0;width:1100px;height:48px;border-bottom:1px solid var(--teal-line)}
.top-links a{position:absolute;top:13px;color:var(--white);font-size:14px;text-decoration:none}
.currency{position:absolute;left:772px;top:13px;color:var(--white);font-size:14px}
.currency svg{vertical-align:middle;margin-left:6px}
.cart-pill{position:absolute;left:952px;top:3px;width:148px;height:32px;background:var(--coral);border:1px solid #f5595b;color:var(--white);font-size:13px;display:flex;align-items:center;padding-left:10px;gap:12px}
.brand{position:absolute;left:50px;top:72px;display:flex;align-items:center;gap:10px;color:var(--white);font-size:40px;font-weight:700}
.brand .dot{width:16px;height:16px;background:var(--coral)}
.main-nav{position:absolute;top:80px;left:653px;height:37px}
.main-nav a{position:absolute;top:0;height:37px;line-height:37px;color:var(--white);font-size:18px;text-decoration:none;white-space:nowrap}
.main-nav .new{background:var(--coral);padding:0 17px;left:0}
.hero{position:absolute;left:50px;top:138px;width:1102px;height:459px;background:linear-gradient(90deg,#4f7a3e 0%,#dfe3e0 18%,#f2f2ee 50%,#dfe3e0 82%,#4f7a3e 100%)}
.hero-photo{position:absolute;inset:0}
.hero-bar{position:absolute;left:0;bottom:0;width:100%;height:45px;background:rgba(40,40,40,.75);display:flex;justify-content:center;align-items:center;gap:14px}
.hero-bar span{width:9px;height:9px;border-radius:50%;background:var(--white)}
.hero-bar span.on{width:16px;height:16px;background:var(--coral)}
.section-head{position:absolute;left:50px;top:606px;width:1102px;height:40px;border-bottom:3px double var(--rule)}
.section-head h2{font-weight:400;font-size:22px;color:var(--teal);line-height:30px}
.arrows{position:absolute;right:0;top:8px;display:flex;gap:12px}
.arrows span{width:19px;height:19px;display:flex;align-items:center;justify-content:center}
.arrows .prev{background:var(--teal)}
.arrows .next{background:var(--coral)}
.product{position:absolute;top:658px;width:264px;height:435px;background:var(--white);border:1px solid #dcdcdc}
.product-photo{position:absolute;left:19px;top:19px;width:225px;height:299px;border:1px solid #ddd}
.product-name{position:absolute;left:20px;top:329px;font-size:13px}
.product-price{position:absolute;left:20px;top:351px;font-size:14px;color:var(--coral)}
.add-cart{position:absolute;left:20px;top:378px;width:135px;height:35px;background:var(--teal);color:var(--white);font-size:16px;display:flex;align-items:center;justify-content:center}
.add-cart.hot{background:var(--coral)}
.icon-btn{position:absolute;top:378px;width:35px;height:35px;background:var(--muted);display:flex;align-items:center;justify-content:center}
</style>
</head>
<body>
<header class="site-header">
  <div class="top-bar">
    <nav class="top-links">
      <a href="#" style="left:0">My Account</a>
      <a href="#" style="left:118px">My Wishlist</a>
      <a href="#" style="left:230px">Login/Register</a>
    </nav>
    <div class="currency">Currency: USD<svg width="10" height="6" viewBox="0 0 10 6"><path d="M1 1l4 4 4-4" stroke="#fff" fill="none"/></svg></div>
    <div class="cart-pill">
      <svg width="14" height="18" viewBox="0 0 14 18"><rect x="1" y="5" width="12" height="12" fill="#fff"/><path d="M4 5V3a3 3 0 016 0v2" stroke="#fff" fill="none" stroke-width="1.5"/></svg>
      <span>0 item(s) - $0,00</span>
    </div>
  </div>
  <div class="brand"><span class="dot"></span>TrelWick</div>
  <nav class="main-nav">
    <a href="#" class="new">NEW!</a>
    <a href="#" style="left:105px">CLOTHING</a>
    <a href="#" style="left:230px">SHOES</a>
    <a href="#" style="left:313px">ACCESORIES</a>
    <a href="#" style="left:451px">BLOG</a>
  </nav>
</header>

<section class="hero">
  <div class="hero-photo" role="img" aria-label="Model in a lavender blouse holding a handbag against white shutters framed by leaves"></div>
  <div class="hero-bar"><span></span><span></span><span class="on"></span><span></span><span></span></div>
</section>

<div class="section-head">
  <h2>New Products</h2>
  <div class="arrows">
    <span class="prev"><svg width="8" height="10" viewBox="0 0 8 10"><path d="M6 1L2 5l4 4" stroke="#fff" fill="none"/></svg></span>
    <span class="next"><svg width="8" height="10" viewBox="0 0 8 10"><path d="M2 1l4 4-4 4" stroke="#fff" fill="none"/></svg></span>
  </div>
</div>

<article class="product" style="left:50px">
  <div class="product-photo" role="img" aria-label="White and nude panelled bodycon dress" style="background:linear-gradient(#f6ece6,#ead7cb)"></div>
  <p class="product-name">Lorem ipsum dolor sit amet</p>
  <p class="product-price">$ 175.00</p>
  <div class="add-cart hot">ADD TO CART</div>
  <div class="icon-btn" style="left:164px"><svg width="14" height="14" viewBox="0 0 14 14"><rect x="1" y="3" width="10" height="10" fill="none" stroke="#ff7b7c"/><path d="M3 7l3 3 7-8" stroke="#ff7b7c" fill="none"/></svg></div>
  <div class="icon-btn" style="left:208px"><svg width="14" height="12" viewBox="0 0 14 12"><path d="M7 12L1 6a3 3 0 015-4l1 1 1-1a3 3 0 015 4z" fill="#ff7b7c"/></svg></div>
</article>

<article class="product" style="left:329px">
  <div class="product-photo" role="img" aria-label="Blue open-back bandage dress" style="background:linear-gradient(#f3f4f8,#5b86d3)"></div>
  <p class="product-name">Lorem ipsum dolor sit amet</p>
  <p class="product-price">$ 175.00</p>
  <div class="add-cart">ADD TO CART</div>
  <div class="icon-btn" style="left:166px"><svg width="14" height="14" viewBox="0 0 14 14"><rect x="1" y="3" width="10" height="10" fill="none" stroke="#46c6c6"/><path d="M3 7l3 3 7-8" stroke="#46c6c6" fill="none"/></svg></div>
  <div class="icon-btn" style="left:210px"><svg width="14" height="12" viewBox="0 0 14 12"><path d="M7 12L1 6a3 3 0 015-4l1 1 1-1a3 3 0 015 4z" fill="#46c6c6"/></svg></div>
</article>

<article class="product" style="left:609px">
  <div class="product-photo" role="img" aria-label="Blue striped short-sleeve bodycon dress" style="background:linear-gradient(#f6f6f8,#3d5fb8 60%,#9fe0e0)"></div>
  <p class="product-name">Lorem ipsum dolor sit amet</p>
  <p class="product-price">$ 175.00</p>
  <div class="add-cart">ADD TO CART</div>
  <div class="icon-btn" style="left:166px"><svg width="14" height="14" viewBox="0 0 14 14"><rect x="1" y="3" width="10" height="10" fill="none" stroke="#46c6c6"/><path d="M3 7l3 3 7-8" stroke="#46c6c6" fill="none"/></svg></div>
  <div class="icon-btn" style="left:210px"><svg width="14" height="12" viewBox="0 0 14 12"><path d="M7 12L1 6a3 3 0 015-4l1 1 1-1a3 3 0 015 4z" fill="#46c6c6"/></svg></div>
</article>

<article class="product" style="left:888px">
  <div class="product-photo" role="img" aria-label="Beige long-sleeve studded bodycon dress" style="background:linear-gradient(#f7f3f0,#e5d6c8)"></div>
  <p class="product-name">Lorem ipsum dolor sit amet</p>
  <p class="product-price">$ 175.00</p>
  <div class="add-cart">ADD TO CART</div>
  <div class="icon-btn" style="left:166px"><svg width="14" height="14" viewBox="0 0 14 14"><rect x="1" y="3" width="10" height="10" fill="none" stroke="#46c6c6"/><path d="M3 7l3 3 7-8" stroke="#46c6c6" fill="none"/></svg></div>
  <div class="icon-btn" style="left:210px"><svg width="14" height="12" viewBox="0 0 14 12"><path d="M7 12L1 6a3 3 0 015-4l1 1 1-1a3 3 0 015 4z" fill="#46c6c6"/></svg></div>
</article>
</body>
</html>
```